Cards and Stationary for natural and holistic Earthing/Grounding products
Solvana Portugal
Cards and Stationary for natural and holistic Earthing/Grounding products - Health
Creative Brief
Bright & Fun-filled
Miro T. Kastelan, PhD
Solvana Portugal Founder
Rua dos Pinheiros Altos 14 2615-117, Vila Serrana, Lusaria
info@solvanaportugal.pt
www.solvanaportugal.pt
The back of the card should incorporate the logo and web address.

```html
<!DOCTYPE html>
<html lang="en">
<head>
<meta charset="utf-8">
<title>Solvana Portugal – Business Card</title>
<link href="https://fonts.googleapis.com/css2?family=Open+Sans:wght@400;600;700&display=swap" rel="stylesheet">
<style>
  :root {
    --stage: #2b2b2b;
    --card: #ffffff;
    --green: #6cb33f;
    --green-dark: #4f8f2a;
    --ink: #3a3a3a;
    --muted: #7a7a7a;
    --grey-mark: #8a8a8a;
    --rule: #d6d6d6;
  }
  * { box-sizing: border-box; margin: 0; padding: 0; }
  html, body { width: 1200px; height: 758px; overflow: hidden; }
  body {
    background: var(--stage);
    font-family: "Open Sans", Arial, sans-serif;
    position: relative;
  }
  .card {
    position: absolute;
    width: 540px;
    height: 310px;
    background: var(--card);
    overflow: hidden;
    box-shadow: 0 10px 24px rgba(0,0,0,.35);
  }
  .card--front { left: 50px; top: 200px; }
  .card--back  { left: 620px; top: 250px; }

  .card__bands { position: absolute; inset: 0; width: 100%; height: 100%; }

  .brand {
    position: absolute;
    display: flex;
    align-items: center;
    gap: 10px;
  }
  .brand__dot { width: 22px; height: 22px; border-radius: 50%; background: var(--green); flex: none; }
  .brand__name {
    font-weight: 700;
    font-size: 30px;
    line-height: 1.05;
    color: var(--green);
  }
  .card--front .brand { left: 38px; top: 112px; }

  .divider {
    position: absolute;
    left: 232px; top: 78px;
    width: 1px; height: 154px;
    background: var(--rule);
  }
  .contact { position: absolute; left: 250px; top: 80px; }
  .contact__name { font-size: 18px; font-weight: 700; color: var(--green); }
  .contact__name .degree { font-weight: 400; color: var(--muted); font-size: 14px; }
  .contact__role { font-size: 12px; color: var(--muted); margin-bottom: 10px; }
  .contact__list { list-style: none; }
  .contact__item {
    display: flex; align-items: flex-start; gap: 8px;
    font-size: 11.5px; line-height: 1.35; color: var(--ink);
    margin-bottom: 5px;
  }
  .contact__item svg { flex: none; width: 12px; height: 12px; margin-top: 2px; fill: var(--ink); }

  .card--back .brand {
    left: 0; right: 0; top: 92px;
    justify-content: center;
  }
  .card--back .brand__dot { background: var(--grey-mark); width: 28px; height: 28px; }
  .card--back .brand__name { color: var(--grey-mark); font-size: 40px; }
  .back__web {
    position: absolute; left: 0; right: 0; top: 236px;
    text-align: center;
    font-size: 17px; font-weight: 700; color: var(--ink);
  }
</style>
</head>
<body>

<section class="card card--front" aria-label="Business card front">
  <svg class="card__bands" viewBox="0 0 540 310" preserveAspectRatio="none" aria-hidden="true">
    <path d="M210 0 H540 V34 H300 C265 34 250 18 210 0 Z" fill="var(--green)"/>
    <path d="M215 0 C245 14 262 26 300 26 H540 V34 H300 C265 34 250 18 215 0 Z" fill="var(--green-dark)" opacity=".35"/>
    <path d="M0 276 H240 C280 276 300 292 330 310 H0 Z" fill="var(--green)"/>
  </svg>

  <div class="brand">
    <span class="brand__dot"></span>
    <span class="brand__name">Solvana<br>Portugal</span>
  </div>

  <div class="divider"></div>

  <div class="contact">
    <p class="contact__name">Miro T. Kastelan, <span class="degree">PhD</span></p>
    <p class="contact__role">Solvana Portugal Founder</p>
    <ul class="contact__list">
      <li class="contact__item">
        <svg viewBox="0 0 12 12"><path d="M3 0h6a1 1 0 0 1 1 1v10a1 1 0 0 1-1 1H3a1 1 0 0 1-1-1V1a1 1 0 0 1 1-1zm0 1.5v8h6v-8z"/></svg>
        +351 912 004 471
      </li>
      <li class="contact__item">
        <svg viewBox="0 0 12 12"><path d="M0 2h12v8H0zm1 1v.4l5 3.2 5-3.2V3zm0 1.6V9h10V4.6L6 7.8z"/></svg>
        info@solvanaportugal.pt
      </li>
      <li class="contact__item">
        <svg viewBox="0 0 12 12"><path d="M6 0a6 6 0 1 0 0 12A6 6 0 0 0 6 0zm0 1a5 5 0 0 1 4.6 3H8.4A7 7 0 0 0 6 1zm-1 0a7 7 0 0 0-1.9 3H1.4A5 5 0 0 1 5 1zM1 6l.1-1h2a8 8 0 0 0 0 2h-2zm4 5a5 5 0 0 1-3.6-3h1.7A7 7 0 0 0 5 11zm1 0a7 7 0 0 0 2.4-3h2.2A5 5 0 0 1 6 11zm2.9-4a8 8 0 0 0 0-2h2l.1 1-.1 1z"/></svg>
        www.solvanaportugal.pt
      </li>
      <li class="contact__item">
        <svg viewBox="0 0 12 12"><path d="M6 0a4 4 0 0 1 4 4c0 3-4 8-4 8S2 7 2 4a4 4 0 0 1 4-4zm0 2.3a1.7 1.7 0 1 0 0 3.4 1.7 1.7 0 0 0 0-3.4z"/></svg>
        <span>Rua dos Pinheiros Altos 14<br>2615-117, Vila Serrana, Lusaria</span>
      </li>
    </ul>
  </div>
</section>

<section class="card card--back" aria-label="Business card back">
  <div class="brand">
    <span class="brand__dot"></span>
    <span class="brand__name">Solvana<br>Portugal</span>
  </div>
  <p class="back__web">www.solvanaportugal.pt</p>
</section>

</body>
</html>
```